A-Stand Directional Sign Design

Objective:
We need a professional graphic design for an A-Stand sign that will guide customers arriving in our parking lot to our office. The design should be visually clear, welcoming, and aligned with our brand identity.
REQUIREMENTS:
Two versions of the design:
- One with an arrow pointing left
- One with an arrow pointing right
(This allows us to place the A-Stand anywhere and flip the graphic as needed.)
DIMENSIONS:
- Viewable Area: 30" x 40"
BRAND ALIGNMENT:
- Colors, fonts, and overall style should match our website: www.skornabel.com
- Clean, modern, and professional look consistent with our aviation/tourism brand
CONTENT:
- Clear directional arrow (left or right depending on version)
- Text: “Office Entrance” or similar concise wording (designers may propose alternatives if they improve clarity)
READABILITY:
- Bold, high-contrast design for visibility from a distance
- Simple layout that avoids clutter
DELIVERABLES:
- Final artwork in print-ready format (PDF preferred)
- Two versions: Arrow Left and Arrow Right
DESIGN GOAL:
Ensure customers can easily find our office upon arrival, while reinforcing skorNABEL’s professional and welcoming brand image.
Target Market(s)
Tourism

```html
<!DOCTYPE html>
<html lang="en">
<head>
<meta charset="utf-8">
<title>skorNABEL – Office Entrance A-Stand Signs</title>
<link href="https://fonts.googleapis.com/css2?family=Roboto+Condensed:wght@900&display=swap" rel="stylesheet">
<style>
  :root {
    --page-bg: #d9dbde;
    --sign-bg: #eef1f4;
    --sign-bg-deep: #e2e7ec;
    --brand-blue: #2878b9;
    --brand-sky: #85aad5;
    --arrow-deep: #3465b2;
    --arrow-bright: #2a95d3;
    --accent-magenta: #be4d87;
    --accent-plum: #93245f;
    --photo-warm: #b89a7c;
    --photo-dark: #3a3148;
    --photo-light: #d9cfc3;
    --white: #ffffff;
  }
  * { margin: 0; padding: 0; box-sizing: border-box; }
  html, body {
    width: 980px; height: 1200px; overflow: hidden;
    background: var(--page-bg);
  }
  .board { position: relative; width: 980px; height: 1200px; }
  .sign {
    position: absolute; left: 151px; width: 678px; height: 509px;
    background: radial-gradient(ellipse at 55% 45%, #f7f9fb 0%, var(--sign-bg) 55%, var(--sign-bg-deep) 100%);
    overflow: hidden;
  }
  .sign--left { top: 69px; }
  .sign--right { top: 625px; }
  .sign-art { position: absolute; inset: 0; width: 100%; height: 100%; }
  .brand {
    position: absolute; top: 112px;
    display: flex; align-items: center; gap: 8px;
    font-family: "Roboto Condensed", sans-serif; font-weight: 900;
    font-size: 30px; line-height: 1;
    color: var(--brand-blue);
  }
  .sign--left .brand { right: 54px; }
  .sign--right .brand { left: 54px; }
  .brand-dot {
    width: 18px; height: 18px; border-radius: 50%;
    background: var(--brand-blue);
  }
  .headline {
    position: absolute; top: 190px;
    font-family: "Roboto Condensed", sans-serif; font-weight: 900;
    text-transform: uppercase; white-space: nowrap;
    font-size: 110px; line-height: 91px; letter-spacing: -1px;
  }
  .sign--left .headline { right: 54px; text-align: right; }
  .sign--right .headline { left: 54px; text-align: left; }
  .headline-office { display: block; color: var(--brand-blue); }
  .headline-entrance { display: block; color: var(--brand-sky); }
</style>
</head>
<body>
<main class="board">

  <section class="sign sign--left" aria-label="Office entrance sign, arrow pointing left">
    <svg class="sign-art" viewBox="0 0 678 509" xmlns="http://www.w3.org/2000/svg">
      <defs>
        <linearGradient id="photoToneL" x1="0" y1="0" x2="1" y2="1">
          <stop offset="0" stop-color="var(--photo-warm)"/>
          <stop offset="0.45" stop-color="var(--photo-dark)"/>
          <stop offset="1" stop-color="var(--photo-light)"/>
        </linearGradient>
        <linearGradient id="arrowToneL" x1="1" y1="0" x2="0" y2="0">
          <stop offset="0" stop-color="var(--arrow-bright)"/>
          <stop offset="0.35" stop-color="var(--arrow-deep)"/>
          <stop offset="1" stop-color="var(--arrow-deep)"/>
        </linearGradient>
        <linearGradient id="magentaToneL" x1="0" y1="0" x2="0" y2="1">
          <stop offset="0" stop-color="var(--accent-magenta)"/>
          <stop offset="1" stop-color="var(--accent-plum)"/>
        </linearGradient>
      </defs>
      <polygon class="accent-sky" points="0,227 69,272 0,323" fill="var(--brand-sky)"/>
      <path class="photo-frame" d="M0,0 H540 L180,262 Q150,285 110,282 Q85,280 60,262 L0,220 Z" fill="var(--white)"/>
      <path class="photo" role="img" aria-label="Photo of two smiling passengers wearing headsets inside a helicopter cabin"
            d="M0,0 H527 L172,255 Q145,275 110,272 Q88,270 66,255 L0,208 Z" fill="url(#photoToneL)"/>
      <polygon class="accent-magenta" points="678,357 678,509 468,509" fill="url(#magentaToneL)"/>
      <polygon class="direction-arrow" points="15,419 116,347 116,395 602,395 536,443 116,443 116,492" fill="url(#arrowToneL)"/>
    </svg>
    <div class="brand"><span class="brand-dot"></span>skornabel.com</div>
    <h2 class="headline">
      <span class="headline-office">Office</span>
      <span class="headline-entrance">Entrance</span>
    </h2>
  </section>

  <section class="sign sign--right" aria-label="Office entrance sign, arrow pointing right">
    <svg class="sign-art" viewBox="0 0 678 509" xmlns="http://www.w3.org/2000/svg">
      <defs>
        <linearGradient id="photoToneR" x1="1" y1="0" x2="0" y2="1">
          <stop offset="0" stop-color="var(--photo-warm)"/>
          <stop offset="0.45" stop-color="var(--photo-dark)"/>
          <stop offset="1" stop-color="var(--photo-light)"/>
        </linearGradient>
        <linearGradient id="arrowToneR" x1="1" y1="0" x2="0" y2="0">
          <stop offset="0" stop-color="var(--arrow-bright)"/>
          <stop offset="0.35" stop-color="var(--arrow-deep)"/>
          <stop offset="1" stop-color="var(--arrow-deep)"/>
        </linearGradient>
        <linearGradient id="magentaToneR" x1="0" y1="0" x2="0" y2="1">
          <stop offset="0" stop-color="var(--accent-magenta)"/>
          <stop offset="1" stop-color="var(--accent-plum)"/>
        </linearGradient>
      </defs>
      <g transform="translate(678,0) scale(-1,1)">
        <polygon class="accent-sky" points="0,227 69,272 0,323" fill="var(--brand-sky)"/>
        <path class="photo-frame" d="M0,0 H540 L180,262 Q150,285 110,282 Q85,280 60,262 L0,220 Z" fill="var(--white)"/>
        <path class="photo" role="img" aria-label="Photo of two smiling passengers wearing headsets inside a helicopter cabin"
              d="M0,0 H527 L172,255 Q145,275 110,272 Q88,270 66,255 L0,208 Z" fill="url(#photoToneR)"/>
        <polygon class="accent-magenta" points="678,357 678,509 468,509" fill="url(#magentaToneR)"/>
        <polygon class="direction-arrow" points="15,419 116,347 116,395 602,395 536,443 116,443 116,492" fill="url(#arrowToneR)"/>
      </g>
    </svg>
    <div class="brand"><span class="brand-dot"></span>skornabel.com</div>
    <h2 class="headline">
      <span class="headline-office">Office</span>
      <span class="headline-entrance">Entrance</span>
    </h2>
  </section>

</main>
</body>
</html>
```